Norvane Builders Business Card

Modern and Professional Business Card for a Med size construction/development company.

See the samples below for the design I like … but I need ideas for incorporating the red company logo while still keeping the clean look of the card samples that are attached.

Logo and tag line on the back … info on the front.

Tagline: Built Right from the Footings Up

Target Market(s)

Med-Large General Contractors

Contact Information for Business Card

Norvane Builders Limited
42 Brenton Street
Elk Harbour, NL
B3K 7T2

t: 709-555-0147
f: 709-555-0192
w: www.norvanebuilders-example.com

Font styles to use
Sans Serif

Colors
fbee3e

Requirements
Must have
• I like the black and yellow designs of the attached samples …. but I'm not sure how to incorporate the red Norvane Builders logo into that design??
Nice to have
• Construction safety strips

```html
<!DOCTYPE html>
<html lang="en">
<head>
<meta charset="utf-8">
<title>Norvane Builders Business Card</title>
<link rel="stylesheet" href="https://fonts.googleapis.com/css2?family=Arimo:wght@700&display=swap">
<style>
  :root {
    --page: #3b3b3b;
    --card: #262626;
    --safety-yellow: #fbee3e;
    --white: #ffffff;
  }
  * { box-sizing: border-box; margin: 0; padding: 0; }
  html, body {
    width: 1200px; height: 1200px; overflow: hidden;
    background: var(--page);
  }
  body {
    font-family: "Arimo", Arial, sans-serif;
    font-weight: 700;
    display: flex; flex-direction: column; align-items: center;
    padding-top: 96px;
    gap: 61px;
  }
  .card {
    position: relative;
    width: 757px; height: 437px;
    background: var(--card);
    box-shadow: 0 16px 36px rgba(0,0,0,.45);
    overflow: hidden;
  }
  .safety-strip {
    position: absolute; left: 0; right: 0; height: 57px;
    background: repeating-linear-gradient(
      120deg,
      var(--safety-yellow) 0 27px,
      var(--card) 27px 56px
    );
  }
  .safety-strip--top { top: 0; }
  .safety-strip--bottom { bottom: 0; }

  /* Logo side */
  .brand {
    position: absolute; top: 168px; left: 0; right: 0;
    display: flex; align-items: center; justify-content: center; gap: 16px;
  }
  .brand__mark { width: 34px; height: 34px; background: var(--safety-yellow); }
  .brand__name {
    color: var(--safety-yellow);
    font-size: 46px; line-height: 56px; text-transform: uppercase;
  }
  .tagline {
    position: absolute; top: 317px; left: 0; right: 0;
    text-align: center; color: var(--safety-yellow);
    font-size: 21px; line-height: 26px; letter-spacing: .3px; text-transform: uppercase;
  }

  /* Info side */
  .contact {
    position: absolute; top: 87px; left: 0; right: 0;
    display: flex; flex-direction: column; align-items: center;
    color: var(--white); text-align: center;
  }
  .company-name {
    color: var(--safety-yellow); font-size: 31px; line-height: 37px; margin-bottom: 21px;
  }
  .address { font-size: 21px; line-height: 29px; font-style: normal; margin-bottom: 22px; }
  .contact-icons { display: flex; gap: 10px; margin-bottom: 7px; }
  .contact-icons svg { width: 26px; height: 26px; }
  .contact-line { font-size: 21px; line-height: 33px; }
</style>
</head>
<body>

  <section class="card card--brand" aria-label="Card logo side">
    <div class="safety-strip safety-strip--top"></div>
    <div class="brand">
      <span class="brand__mark"></span>
      <span class="brand__name">Norvane Builders</span>
    </div>
    <p class="tagline">Built Right from the Footings Up</p>
    <div class="safety-strip safety-strip--bottom"></div>
  </section>

  <section class="card card--info" aria-label="Card contact side">
    <div class="safety-strip safety-strip--top"></div>
    <div class="contact">
      <h1 class="company-name">Norvane Builders Limited</h1>
      <address class="address">42 Brenton Street Elk Harbour,<br>NL B3K 7T2</address>
      <div class="contact-icons" aria-hidden="true">
        <svg viewBox="0 0 30 30">
          <circle cx="15" cy="15" r="13" fill="none" stroke="#fbee3e" stroke-width="2"/>
          <path d="M8 12c0-2 3-3 7-3s7 1 7 3v1.5h-3.5V12h-7v1.5H8z M9.5 15h11l1 6h-13z" fill="#fbee3e"/>
        </svg>
        <svg viewBox="0 0 30 30">
          <circle cx="15" cy="15" r="13" fill="none" stroke="#fbee3e" stroke-width="2"/>
          <rect x="10" y="7.5" width="10" height="5" fill="#fbee3e"/>
          <rect x="7.5" y="13" width="15" height="7" rx="1" fill="#fbee3e"/>
          <rect x="10" y="20" width="10" height="3" fill="#fbee3e"/>
        </svg>
        <svg viewBox="0 0 30 30">
          <circle cx="15" cy="15" r="13" fill="none" stroke="#fbee3e" stroke-width="2"/>
          <circle cx="15" cy="15" r="8" fill="none" stroke="#fbee3e" stroke-width="1.6"/>
          <ellipse cx="15" cy="15" rx="3.5" ry="8" fill="none" stroke="#fbee3e" stroke-width="1.6"/>
          <path d="M7 15h16 M8.5 11h13 M8.5 19h13" stroke="#fbee3e" stroke-width="1.4"/>
        </svg>
      </div>
      <p class="contact-line">709-555-0147</p>
      <p class="contact-line">709-555-0192</p>
      <p class="contact-line">www.norvanebuilders-example.com</p>
    </div>
    <div class="safety-strip safety-strip--bottom"></div>
  </section>

</body>
</html>
```